Machining Business Order Thank You Insert

I am looking for a business style card to include with orders that I ship. The card needs to thank the recipient for their order, and encourage them to leave a review. The card should include my business name and contact information and have an area to hand write a message.

I mainly sale on Craftory and my own website. We are a machining an manufacturing business that are in the sale of mostly metal machined and 3d printed plastic products.

The front of the card should include the following:
Logo: (attached)
Instagram: https://www.instagram.com/kelvorn/
Facebook: https://www.facebook.com/Kelvorn
Website: https://www.kelvorn-example.com/

The back of the card needs an area to write a message

Industry/Entity Type

3D Printing, Machining, Craftory

Contact Information for Business Card

Black or white front, white back to write a personal message

Font styles to use
Sans Serif

Colors

Designer to choose colors to be used in the design.

Requirements
Must have
• Encourage a review, social media info

```html
<!DOCTYPE html>
<html lang="en">
<head>
<meta charset="utf-8">
<title>Kelvorn Order Thank You Insert</title>
<link rel="stylesheet" href="https://fonts.googleapis.com/css2?family=Rajdhani:wght@600&family=Roboto:wght@400;500&display=swap">
<style>
  :root {
    --backdrop: #242424;
    --card: #1f1c23;
    --card-edge: #19161c;
    --frame-shadow: #121014;
    --accent: #f05a22;
    --steel: #7d7b80;
    --text-light: #ecebee;
    --text-muted: #8a878e;
    --note-paper: #ffffff;
    --note-rule: #d9d7dc;
    --note-label: #9a979e;
  }
  * { margin: 0; padding: 0; box-sizing: border-box; }
  html, body {
    width: 1200px; height: 874px; overflow: hidden;
    background: var(--backdrop);
  }
  .canvas { position: relative; width: 1200px; height: 874px; }

  .card {
    position: absolute; left: 320px; width: 560px; height: 320px;
    background: var(--card-edge);
    box-shadow: 0 18px 40px rgba(0,0,0,.55);
  }
  .card--note { top: 87px; }
  .card--contact { top: 467px; }

  .card__panel {
    position: absolute; inset: 18px;
    background: var(--card);
    border: 3px solid var(--frame-shadow);
  }

  .accent-bar { position: absolute; background: var(--accent); }
  .steel-bar { position: absolute; background: var(--steel); }
  .card--note .accent-bar { top: 15px; left: 15px; width: 200px; height: 4px; }
  .card--note .steel-bar { top: 15px; left: 15px; width: 3px; height: 120px; }
  .card--contact .accent-bar { bottom: 15px; right: 15px; width: 220px; height: 4px; }
  .card--contact .steel-bar { bottom: 15px; right: 15px; width: 3px; height: 130px; }

  .wordmark {
    font-family: "Rajdhani", sans-serif;
    font-weight: 600;
    letter-spacing: 0.32em;
    text-transform: uppercase;
  }

  /* Thank-you card with handwriting area */
  .card--note .wordmark {
    position: absolute; left: 0; right: 0; top: 18px;
    text-align: center; font-size: 22px; color: var(--steel);
  }
  .thank-you {
    position: absolute; left: 0; right: 0; top: 54px;
    text-align: center;
    font-family: "Roboto", sans-serif; font-weight: 500;
    font-size: 17px; color: var(--text-light);
  }
  .thank-you__accent { color: var(--accent); }
  .note-area {
    position: absolute; left: 36px; right: 36px; top: 90px; bottom: 24px;
    background: var(--note-paper);
    padding: 12px 18px 0;
  }
  .note-area__label {
    font-family: "Roboto", sans-serif; font-size: 10px;
    letter-spacing: 0.12em; text-transform: uppercase;
    color: var(--note-label);
  }
  .note-area__rule {
    display: block; height: 1px; background: var(--note-rule);
    margin-top: 30px;
  }
  .note-area__rule:first-of-type { margin-top: 28px; }

  /* Contact card */
  .brand-block {
    position: absolute; left: 60px; top: 100px;
    display: flex; align-items: center; gap: 12px;
  }
  .brand-block__square { width: 14px; height: 14px; background: var(--accent); }
  .card--contact .wordmark { font-size: 22px; color: var(--accent); }

  .divider {
    position: absolute; left: 245px; top: 66px;
    width: 1px; height: 120px; background: var(--text-muted);
  }

  .contact-list {
    position: absolute; left: 268px; top: 76px;
    list-style: none;
    font-family: "Roboto", sans-serif; font-size: 14px;
    color: var(--text-light);
  }
  .contact-list li { display: flex; align-items: center; gap: 9px; height: 22px; }
  .contact-list .location { margin-bottom: 12px; }
  .contact-icon { width: 12px; height: 12px; flex: none; }
  .contact-dot { width: 11px; height: 11px; border-radius: 50%; background: var(--accent); flex: none; }

  .review-prompt {
    position: absolute; left: 0; right: 0; top: 214px;
    text-align: center;
    font-family: "Roboto", sans-serif; font-size: 13px;
    color: var(--text-muted);
  }
  .review-prompt strong { color: var(--accent); font-weight: 500; }
</style>
</head>
<body>
<main class="canvas">

  <section class="card card--note" aria-label="Thank you card with note area">
    <div class="card__panel">
      <p class="wordmark">Kelvorn</p>
      <p class="thank-you">Thank you for your <span class="thank-you__accent">order!</span></p>
      <div class="note-area" aria-label="Space for a handwritten message">
        <p class="note-area__label">A note for you</p>
        <span class="note-area__rule"></span>
        <span class="note-area__rule"></span>
        <span class="note-area__rule"></span>
      </div>
    </div>
    <span class="accent-bar"></span>
    <span class="steel-bar"></span>
  </section>

  <section class="card card--contact" aria-label="Contact card">
    <div class="card__panel">
      <div class="brand-block">
        <span class="brand-block__square"></span>
        <p class="wordmark">Kelvorn</p>
      </div>
      <span class="divider"></span>
      <ul class="contact-list">
        <li class="location">
          <svg class="contact-icon" viewBox="0 0 12 12" aria-hidden="true">
            <path d="M6 0.5a4 4 0 0 1 4 4c0 3-4 7-4 7s-4-4-4-7a4 4 0 0 1 4-4z" fill="var(--accent)"/>
            <circle cx="6" cy="4.5" r="1.5" fill="var(--card)"/>
          </svg>
          Harlow Falls, IN
        </li>
        <li><span class="contact-dot"></span>@kelvorn</li>
        <li><span class="contact-dot"></span>/kelvorn</li>
        <li>
          <svg class="contact-icon" viewBox="0 0 12 12" aria-hidden="true">
            <circle cx="6" cy="6" r="5.5" fill="var(--accent)"/>
            <path d="M0.8 6h10.4M6 0.5c-2 2.5-2 8.5 0 11M6 0.5c2 2.5 2 8.5 0 11" stroke="var(--card)" stroke-width="0.9" fill="none"/>
          </svg>
          kelvorn-example.com
        </li>
      </ul>
      <p class="review-prompt">Loved your order? Please <strong>leave us a review</strong> on Craftory.</p>
    </div>
    <span class="accent-bar"></span>
    <span class="steel-bar"></span>
  </section>

</main>
</body>
</html>
```